Business Card Design

Quiet Fernlight - edgy, unique, ontrend clothing for girls 0-12.
I would like simple styling with white background and natural beige/brown font, similar to attached font.

Industry/Entity Type

Clothing

Contact Information for Business Card

Hi, I would like a very simple business card, white background with natural, beige, brown font, Quiet Fernlight. I design and sell clothes for girls 0-12 with a touch of bohemian styling. I would like "Quiet Fernlight" on front and on back -
www.quietfernlight.example.au
Colette Brennick,
0491558213,
colettebrennick@mailvale.example.au

```html
<!DOCTYPE html>
<html lang="en">
<head>
<meta charset="utf-8">
<title>Quiet Fernlight – Business Cards</title>
<link rel="stylesheet" href="https://fonts.googleapis.com/css2?family=Andika:wght@400&family=Mystery+Quest&display=swap">
<style>
  :root {
    --stage: #eef1f2;
    --card: #ffffff;
    --ink-beige: #c6b48f;
    --card-shadow: rgba(40, 50, 55, 0.28);
    --sea-light: #e4eeee;
    --sea-mid: #b9cfd0;
    --sand: #cfc2ae;
  }
  * { box-sizing: border-box; margin: 0; padding: 0; }
  html, body {
    width: 1200px;
    height: 927px;
    overflow: hidden;
    background: var(--stage);
  }
  .stage {
    position: relative;
    width: 1200px;
    height: 927px;
  }
  .card {
    position: absolute;
    width: 680px;
    height: 410px;
    background: var(--card);
    box-shadow: 6px 8px 14px var(--card-shadow);
    overflow: hidden;
    color: var(--ink-beige);
  }
  .card--front { left: 40px; top: 45px; }
  .card--back  { left: 455px; top: 476px; }

  .brand-name {
    font-family: "Mystery Quest", cursive;
    font-weight: 400;
    text-transform: uppercase;
    color: var(--ink-beige);
    line-height: 1;
    white-space: nowrap;
  }
  .tagline {
    font-family: "Andika", sans-serif;
    color: var(--ink-beige);
    white-space: nowrap;
  }

  /* Front */
  .front-photo {
    position: absolute;
    right: 0;
    top: 0;
    width: 420px;
    height: 100%;
    background:
      linear-gradient(to right, var(--card) 0%, rgba(255,255,255,0.6) 30%, rgba(255,255,255,0) 60%),
      linear-gradient(to bottom, var(--sea-light) 0%, var(--sea-mid) 45%, var(--sea-light) 62%, var(--sand) 100%);
  }
  .front-brand {
    position: absolute;
    left: 42px;
    top: 180px;
  }
  .front-brand .brand-name { font-size: 58px; }
  .front-brand .tagline {
    font-size: 21px;
    margin-top: 10px;
    padding-left: 62px;
  }

  /* Back */
  .back-content {
    position: absolute;
    inset: 0;
    text-align: center;
    padding-top: 36px;
  }
  .back-content .brand-name { font-size: 72px; }
  .back-content .tagline {
    font-size: 22px;
    margin-top: 22px;
  }
  .contact-list {
    list-style: none;
    margin-top: 42px;
    font-family: "Andika", sans-serif;
    font-size: 22px;
    line-height: 42px;
  }
</style>
</head>
<body>
<main class="stage">
  <section class="card card--front" aria-label="Business card front">
    <div class="front-photo" role="img" aria-label="Photograph of a young girl in a white dress walking barefoot along the shoreline"></div>
    <div class="front-brand">
      <h1 class="brand-name">Quiet Fernlight</h1>
      <p class="tagline">beautiful clothing for girls 0-12</p>
    </div>
  </section>

  <section class="card card--back" aria-label="Business card back">
    <div class="back-content">
      <h2 class="brand-name">Quiet Fernlight</h2>
      <p class="tagline">beautiful clothing for girls 0-12</p>
      <ul class="contact-list">
        <li class="contact-name">Colette Brennick</li>
        <li class="contact-phone">t: 0491558213</li>
        <li class="contact-email">e: colettebrennick@mailvale.example.au</li>
        <li class="contact-web">w: www.quietfernlight.example.au</li>
      </ul>
    </div>
  </section>
</main>
</body>
</html>
```